Email footer for a cafe

The task is to design an email footer for a new start up cafe business. The logo has been designed, but we would like a professional email footer to sign off on all emails.

The email footer should :
1. look professional and competent
2. be clean and easy to read
3. the email must have the ability to optimise / adjust across the bottom of the email depending on the device being used to read the email
4. the design may stretch across the entire bottom of the email, but this is not mandatory
5. it must incorporate the logo and the details as listed below.
6. For any additional lines / dividers that a designer might choose to incorporate into the email footer, our preference is to match the colour of the logo.

The logo is attached. The logo details are:

The CMYK for the logo is C0 M50 Y100 K0 in font BankGothic Lt BT - Light
The CMKY for the text is C75 M68 Y67 K89 in font AvantGarde Bk BT - Book

The details to be included in the email footer are:

Pim Arlow
Founder
0417 286 314
pimarlow@bramblekitchenvq.com
Unit 6, 14 Talvery Crescelt
Wexholm TLB 5162

Have fun and thank you in advance for choosing to work on our job.

Reason: Thank you to everyone who has submitted their designs for an email footer. Looking at the designs most have been designed horizontally. Could I please also see some designs where all the elements are under each other in a stacked format. I have attached 2 images which I have grabbed from the internet to be used as an example.

```html
<!DOCTYPE html>
<html lang="en">
<head>
<meta charset="utf-8">
<title>Bramble Kitchen – Email Footer</title>
<link rel="stylesheet" href="https://fonts.googleapis.com/css2?family=Jost:wght@400;600&display=swap">
<style>
  :root {
    --wood-dark: #2a1408;
    --wood-mid: #6b3a1a;
    --wood-light: #9a5a2c;
    --panel: #ffffff;
    --brand-orange: #f28a1e;
    --ink: #0e0e0e;
    --divider: #e6e2de;
  }
  * { margin: 0; padding: 0; box-sizing: border-box; }
  html, body {
    width: 1200px;
    height: 363px;
    overflow: hidden;
  }
  body {
    position: relative;
    font-family: "Jost", sans-serif;
    color: var(--ink);
    background: var(--wood-dark);
  }
  .wood-backdrop {
    position: absolute;
    inset: 0;
    background:
      radial-gradient(ellipse at 50% 0%, rgba(255,200,140,0.35), transparent 60%),
      linear-gradient(90deg, var(--wood-dark) 0%, var(--wood-mid) 18%, var(--wood-light) 50%, var(--wood-mid) 82%, var(--wood-dark) 100%);
  }
  .footer-card {
    position: absolute;
    left: 29px;
    top: 51px;
    width: 1131px;
    height: 275px;
    background: var(--panel);
    box-shadow: 0 2px 6px rgba(0,0,0,0.35);
  }
  .accent-bar {
    position: absolute;
    left: 0;
    bottom: 0;
    width: 100%;
    height: 11px;
    background: var(--brand-orange);
  }
  .brand-name {
    position: absolute;
    left: 44px;
    top: 168px;
    width: 280px;
    text-align: center;
    font-size: 30px;
    font-weight: 400;
    letter-spacing: 2px;
    text-transform: uppercase;
    color: var(--brand-orange);
    line-height: 1;
  }
  .divider {
    position: absolute;
    top: 102px;
    width: 2px;
    height: 100px;
    background: linear-gradient(180deg, transparent, var(--divider) 20%, var(--divider) 80%, transparent);
  }
  .divider--first { left: 378px; }
  .divider--second { left: 670px; }
  .contact-person {
    position: absolute;
    left: 406px;
    top: 120px;
  }
  .person-name {
    font-size: 27px;
    line-height: 34px;
  }
  .person-name strong { font-weight: 600; }
  .person-role { font-weight: 400; font-size: 25px; }
  .detail-line {
    font-size: 20px;
    line-height: 30px;
    letter-spacing: 0.3px;
  }
  .detail-label {
    color: var(--brand-orange);
    margin-right: 6px;
  }
  .contact-person .detail-line { margin-top: 10px; margin-left: 4px; }
  .contact-reach {
    position: absolute;
    left: 690px;
    top: 105px;
  }
  .contact-reach .address { margin-top: 10px; display: flex; }
  .address-lines { display: flex; flex-direction: column; }
</style>
</head>
<body>
  <div class="wood-backdrop" role="img" aria-label="Warm wooden plank background"></div>

  <section class="footer-card">
    <div class="brand-name">Bramble Kitchen</div>

    <div class="divider divider--first"></div>

    <div class="contact-person">
      <p class="person-name"><strong>Pim Arlow</strong><span class="person-role">, Founder</span></p>
      <p class="detail-line"><span class="detail-label">P:</span>0417 286 314</p>
    </div>

    <div class="divider divider--second"></div>

    <div class="contact-reach">
      <p class="detail-line"><span class="detail-label">E:</span>pimarlow@bramblekitchenvq.com</p>
      <p class="detail-line address">
        <span class="detail-label">A:</span>
        <span class="address-lines">
          <span>Unit 6, 14 Talvery Crescelt</span>
          <span>Wexholm TLB 5162</span>
        </span>
      </p>
    </div>

    <div class="accent-bar"></div>
  </section>
</body>
</html>
```